Stationery Design Project

We are a start up wine business based in Sydney Australia. We already have a logo and are in the process of completing our website. We require our logo to be cleverly and artfully incorporated into our stationary requirements. Which will initially begin with a company letter head.
As we desire consistency across our brand, we will also be wanting to develop banner advertisements and brochure with the same "look".
If outstanding we move design brief to banner advertisement for web and banner of the website itself.
Older wealthy predominantly male demographic
Business

```html
<!DOCTYPE html>
<html lang="en">
<head>
<meta charset="utf-8">
<title>Ashgrove Wine Co. — Letterhead</title>
<link rel="stylesheet" href="https://fonts.googleapis.com/css2?family=Arimo:wght@400&display=swap">
<style>
  :root {
    --paper: #ffffff;
    --band-dark: #6e6e6e;
    --band-mid: #a9a9a9;
    --band-light: #ececec;
    --rule: #111111;
    --brand: #1a1a1a;
    --contact: #8a8a8a;
  }
  * { margin: 0; padding: 0; box-sizing: border-box; }
  html, body {
    width: 1019px;
    height: 1200px;
    overflow: hidden;
    background: var(--paper);
  }
  .letterhead {
    position: relative;
    width: 1019px;
    height: 1200px;
    background: var(--paper);
    font-family: "Arimo", Arial, sans-serif;
  }
  .side-band {
    position: absolute;
    left: 0;
    top: 0;
    width: 160px;
    height: 1200px;
  }
  .brand {
    position: absolute;
    top: 70px;
    left: 0;
    width: 100%;
    text-align: center;
    display: flex;
    align-items: center;
    justify-content: center;
    gap: 12px;
    color: var(--brand);
    font-size: 30px;
    font-weight: 400;
    letter-spacing: 1px;
  }
  .brand-mark {
    width: 14px;
    height: 14px;
    background: var(--brand);
  }
  .contact {
    position: absolute;
    top: 1128px;
    left: 0;
    width: 100%;
    color: var(--contact);
    font-size: 16px;
    line-height: 26px;
  }
  .contact-col {
    position: absolute;
    top: 0;
  }
  .contact-address { left: 259px; }
  .contact-phone { left: 491px; }
  .contact-web { left: 713px; }
  .contact-line {
    display: flex;
    align-items: center;
    gap: 6px;
    white-space: nowrap;
  }
  .contact-icon {
    width: 13px;
    height: 13px;
    fill: var(--contact);
  }
</style>
</head>
<body>
  <main class="letterhead">
    <svg class="side-band" viewBox="0 0 160 1200" aria-hidden="true">
      <defs>
        <linearGradient id="bandShade" x1="0" y1="0" x2="1" y2="0">
          <stop offset="0" stop-color="var(--band-dark)"/>
          <stop offset="0.45" stop-color="var(--band-mid)"/>
          <stop offset="1" stop-color="var(--band-light)"/>
        </linearGradient>
      </defs>
      <path d="M0 0 H136 C78 320 62 780 132 1200 H0 Z" fill="url(#bandShade)"/>
      <path d="M142 0 C84 320 68 780 138 1200" fill="none" stroke="var(--rule)" stroke-width="2.5"/>
    </svg>

    <header class="brand">
      <span class="brand-mark"></span>
      <span class="brand-name">Ashgrove Wine Co.</span>
    </header>

    <footer class="contact">
      <div class="contact-col contact-address">
        <div class="contact-line">Street Name, City,</div>
        <div class="contact-line">State, zip code</div>
      </div>
      <div class="contact-col contact-phone">
        <div class="contact-line">
          <svg class="contact-icon" viewBox="0 0 16 16" aria-hidden="true"><path d="M3.5 1 L6 1 L7 4.5 L5.3 5.6 C6 7.6 8.4 10 10.4 10.7 L11.5 9 L15 10 L15 12.5 C15 14 13.8 15 12.5 15 C6.5 14.5 1.5 9.5 1 3.5 C1 2.2 2 1 3.5 1 Z"/></svg>
          <span>123-456-7890</span>
        </div>
        <div class="contact-line">
          <svg class="contact-icon" viewBox="0 0 16 16" aria-hidden="true"><rect x="4" y="1" width="8" height="5"/><rect x="1" y="6" width="14" height="7" rx="1.5"/><rect x="4" y="11" width="8" height="4"/></svg>
          <span>123-456-7890</span>
        </div>
      </div>
      <div class="contact-col contact-web">
        <div class="contact-line">
          <svg class="contact-icon" viewBox="0 0 16 16" aria-hidden="true"><rect x="1" y="3" width="14" height="10" rx="1"/><path d="M1.5 3.5 L8 9 L14.5 3.5" fill="none" stroke="#fff" stroke-width="1.4"/></svg>
          <span>hello@ashgrovewine.com</span>
        </div>
        <div class="contact-line">
          <svg class="contact-icon" viewBox="0 0 16 16" aria-hidden="true"><circle cx="8" cy="8" r="7"/><path d="M1 8 H15 M8 1 C4.5 4.5 4.5 11.5 8 15 M8 1 C11.5 4.5 11.5 11.5 8 15" fill="none" stroke="#fff" stroke-width="1.1"/></svg>
          <span>www.ashgrovewine.com</span>
        </div>
      </div>
    </footer>
  </main>
</body>
</html>
```